Cannabis packaging label for a medicine bottle

This label will be for packaged cannabis. There are certain regulations that I will need incorporated such as warning symbols and mandatory wording on the label. The label will be for a medicine canister the measurements are 2 x 4.75. The primary photo will be in the center of the label. Please see photos attached of example label and also a photo of the container.

Product name: “Tovi Lark”.....”Cannabis Flower”...”California Grown”

Target Market(s)

Young and older adults with a conservative sophisticated feel.

Font styles to use
Serif

Colors

Designer to choose colors to be used in the design.

Requirements
Must have
• Primary panel is the part of a cannabis product label that is most likely to be displayed, presented, shown, or examined under customary conditions of display for retail sale.
• Informational panel is any part of the cannabis product label that is not the primary panel and that contains required labeling information.
• All labels must be unobstructed and conspicuous, so the consumer can easily read the labels. The required information shall be located on the outside container or wrapper of the finished product and must have the following information, in no less that 6-point font.
• Primary Panel – All Products:
• Identity of product.
• Universal symbol (must be in black and white).
• Net weight 3.5 grams or volume of the contents in the package.
• Informational Panel – All Products:
• The applicable Government Warning.
• The CA Universal Symbol )may be no smaller than half (.5) inch by x half (.5) inch.)
• This is the applicable government warning for all flower products.
• Primary Panel – Manufactured Goods:
• The THC/CBD contents for the entire contents of the package in milligrams.
• Informational Panel – Manufactured Goods:
• Licensed manufacturer name and contact phone number or web address.
Nice to have
• Modern design but you and hip. Spray paint mame “Tovi Lark”
Should not have
• Should not be appealing to children

```html
<!DOCTYPE html>
<html lang="en">
<head>
<meta charset="utf-8">
<title>Tovi Lark – Cannabis Flower Label</title>
<link href="https://fonts.googleapis.com/css2?family=Permanent+Marker&family=Luckiest+Guy&family=Roboto+Condensed:wght@400;700&display=swap" rel="stylesheet">
<style>
  :root {
    --page: #f2f2f2;
    --wall-teal: #2f6f78;
    --wall-red: #b8382c;
    --wall-orange: #c9782c;
    --wall-purple: #5a3a6a;
    --wall-dark: #3a2a22;
    --lime: #b8e02a;
    --leaf: #4f8f2a;
    --white: #ffffff;
    --alert: #e0201c;
    --ink: #111111;
    --panel-shade: rgba(25, 15, 12, 0.82);
  }
  * { box-sizing: border-box; margin: 0; padding: 0; }
  html, body { width: 889px; height: 1200px; overflow: hidden; }
  body {
    background: var(--page);
    font-family: "Roboto Condensed", sans-serif;
    display: flex; flex-direction: column; align-items: center;
    gap: 20px; padding-top: 20px;
  }
  .label {
    position: relative;
    width: 535px; height: 570px;
    overflow: hidden;
    box-shadow: 0 6px 14px rgba(0,0,0,0.25);
  }
  .label__wall {
    position: absolute; inset: 0;
    background:
      radial-gradient(ellipse at 20% 30%, rgba(47,111,120,0.9), transparent 55%),
      radial-gradient(ellipse at 80% 25%, rgba(90,58,106,0.85), transparent 55%),
      radial-gradient(ellipse at 30% 80%, rgba(184,56,44,0.85), transparent 55%),
      radial-gradient(ellipse at 85% 75%, rgba(201,120,44,0.8), transparent 55%),
      var(--wall-dark);
  }
  .ca-symbol { position: absolute; width: 44px; height: 44px; }
  /* primary panel */
  .primary .ca-symbol { top: 20px; right: 16px; }
  .primary__artwork {
    position: absolute; left: 95px; top: 25px; width: 345px; height: 300px;
    border-radius: 45% 45% 30% 30%;
    background: radial-gradient(ellipse at 50% 45%, #8a6a4a 0%, #4f8f2a 55%, rgba(79,143,42,0.2) 80%, transparent 100%);
  }
  .primary__ribbon {
    position: absolute; left: 195px; top: 288px; width: 165px; height: 30px;
    background: #f3ecd8; border: 2px solid var(--ink); border-radius: 4px;
    transform: rotate(-8deg);
    font-family: "Luckiest Guy", sans-serif; font-size: 13px; color: #1d3aa0;
    display: flex; align-items: center; justify-content: center; letter-spacing: 0.5px;
  }
  .primary__name {
    position: absolute; left: 0; right: 0; top: 318px; text-align: center;
    font-family: "Permanent Marker", cursive; font-size: 96px; line-height: 1;
    color: var(--lime);
  }
  .primary__origin {
    position: absolute; left: 0; right: 0; top: 448px; text-align: center;
    font-family: "Luckiest Guy", sans-serif; font-size: 38px; color: var(--white);
    letter-spacing: 0.5px;
  }
  .pill {
    position: absolute; left: 50%; transform: translateX(-50%);
    background: var(--ink); color: var(--alert);
    font-family: "Luckiest Guy", sans-serif; font-size: 16px;
    padding: 4px 18px 2px; border-radius: 14px; white-space: nowrap;
  }
  .primary .pill { top: 505px; }
  /* information panel */
  .info__name {
    position: absolute; left: 0; right: 0; top: 28px; text-align: center;
    font-family: "Permanent Marker", cursive; font-size: 74px; line-height: 1;
    color: var(--lime);
  }
  .info__prop {
    position: absolute; left: 0; right: 0; top: 128px; text-align: center;
    font-family: "Luckiest Guy", sans-serif; font-size: 20px; color: var(--white);
  }
  .info__box {
    position: absolute; left: 95px; top: 172px; width: 350px; height: 325px;
    background: var(--panel-shade);
    padding: 12px 16px; color: var(--white);
    font-size: 10px; line-height: 1.55;
  }
  .warning-head {
    display: flex; align-items: center; gap: 8px;
    color: var(--alert); font-weight: 700; font-size: 14px; margin-bottom: 4px;
  }
  .warning-head::before, .warning-head::after {
    content: ""; flex: 1; height: 1px; background: var(--alert);
  }
  .prop65 { text-align: center; }
  .prop65 strong { display: block; }
  .gov { margin-top: 22px; }
  .gov b { color: var(--alert); }
  .info__facts {
    display: flex; align-items: center; gap: 22px; margin-top: 14px;
    font-size: 16px; font-weight: 700; line-height: 1.3;
  }
  .info__facts .ca-symbol { position: static; width: 46px; height: 46px; margin-left: auto; }
  .info .pill { top: 520px; }
</style>
</head>
<body>

<section class="label primary">
  <div class="label__wall" role="img" aria-label="Weathered brick wall spray-painted in teal, red, orange and purple"></div>
  <svg class="ca-symbol" viewBox="0 0 44 44" aria-label="California universal cannabis symbol">
    <path d="M22 4 L40 36 H4 Z" fill="none" stroke="#fff" stroke-width="3" stroke-linejoin="round"/>
    <rect x="20.5" y="15" width="3" height="10" fill="#fff"/>
    <circle cx="22" cy="29" r="1.8" fill="#fff"/>
    <text x="22" y="44" text-anchor="middle" font-family="Roboto Condensed, sans-serif" font-weight="700" font-size="8" fill="#fff">CA</text>
  </svg>
  <div class="primary__artwork" role="img" aria-label="Illustrated mascot in a striped knit cap and sunglasses framed by cannabis leaves"></div>
  <div class="primary__ribbon">CANNABIS FLOWER</div>
  <div class="primary__name">Tovi Lark</div>
  <div class="primary__origin">CALIFORNIA GROWN</div>
  <div class="pill">NET WEIGHT 3.5 GRAMS</div>
</section>

<section class="label info">
  <div class="label__wall" role="img" aria-label="Weathered brick wall spray-painted in teal, red, orange and purple"></div>
  <div class="info__name">Tovi Lark</div>
  <div class="info__prop">CALIFORNIA PROPOSITION 65</div>
  <div class="info__box">
    <div class="warning-head">WARNING</div>
    <p class="prop65">This product contains chemicals known to the State of California to cause cancer and birth defects or other reproductive harm. (California Law requires this warning to be given to customers in the State of California.)
      <strong>CALIFORNIA HEALTH &amp; SAFETY CODE SECTION 25249.6</strong></p>
    <p class="gov"><b>GOVERNMENT WARNING:</b> This product contains Cannabis, a Schedule I controlled substance. Keep out of reach of children and animals. Cannabis products may only be possessed or consumed by persons 21 years of age or older unless the person is a qualified patient. The intoxicating effects of cannabis products may be delayed up to two hours. Cannabis use while pregnant or breastfeeding may be harmful. Consumption of Cannabis products impairs your ability to drive and operate machinery. Please use extreme caution.</p>
    <div class="info__facts">
      <div>THC: 78.2%<br>CBD: 2.5%</div>
      <div>Packaged on: date<br>Batch #000000</div>
      <svg class="ca-symbol" viewBox="0 0 44 44" aria-label="California universal cannabis symbol">
        <path d="M22 4 L40 36 H4 Z" fill="none" stroke="#fff" stroke-width="3" stroke-linejoin="round"/>
        <rect x="20.5" y="15" width="3" height="10" fill="#fff"/>
        <circle cx="22" cy="29" r="1.8" fill="#fff"/>
        <text x="22" y="44" text-anchor="middle" font-family="Roboto Condensed, sans-serif" font-weight="700" font-size="8" fill="#fff">CA</text>
      </svg>
    </div>
  </div>
  <div class="pill">WWW.LARKFIELDCO.COM</div>
</section>

</body>
</html>
```